Speisekarten-Design für SportsBar
Zielgruppe
Wir sind moderne SportsBar eines 2.Bundesligisten mit breitem Publikum auch ausserhalb der Fussballs. Wir haben Salate, Burger, Schnitzel und Steaks sowie eine gut sortierte Getränkekarte.
Aufgabenstellung
Für unsere Restaurant Ahornstube SportsBar suchen wir eine neue Speisekarte (Alte Speisekarte ist angehängt)
Wir haben uns für das Format A4 im Clipboard entschieden, da wir flexibel sein möchten, auch wenn sich mal etwas ändern sollte, wir somit eine Seite austauschen können. Auch wollen wir mit einer Wochenkarte arbeiten, die auf der zweiten Seite anhängen sollte.
Wir wünschen uns ein sportlich modernes Design, mit Speisefotos und Sportfotos im Mix als Eyecatcher.
Die Seite für den Kaffe wird nicht benötigt, da wir diese von unserem Partner als fertige Vorlage bekommen(Seite hängt an).
Logos der Getränkemarken sind ebenfalls im Anhang. Aller anderen Fotos etc. können sofort bei Bedarf geliefert werden.
Für den ersten Entwurf würde ich gerne 3-5 Seiten sehen wollen, dabei sind wichtig !
- Titelseite
- Brunch & Buffetseite
- Schnitzelseite
- Burgerseite
- Getränke(Bier)
Vielen Dank, für fragen stehe ich jederzeit zur Verfügung

```html
<!DOCTYPE html>
<html lang="de">
<head>
<meta charset="utf-8">
<title>Burgerseite – Ahornstube SportsBar</title>
<link href="https://fonts.googleapis.com/css2?family=Arimo:wght@400&family=Montserrat:wght@600&family=Exo+2:ital,wght@1,900&display=swap" rel="stylesheet">
<style>
  :root {
    --bg: #0f1822;
    --ink: #ffffff;
    --rule: #3a4552;
    --tab-ink: #0f1822;
    --photo-a: #3a2a22;
    --photo-b: #1a1c20;
  }
  * { margin: 0; padding: 0; box-sizing: border-box; }
  html, body { width: 849px; height: 1200px; overflow: hidden; background: var(--bg); }
  .page {
    position: relative; width: 849px; height: 1200px; overflow: hidden;
    background: var(--bg); color: var(--ink);
    font-family: "Arimo", Arial, sans-serif;
  }
  .hero-photo {
    position: absolute; left: 440px; top: 230px; width: 420px; height: 800px;
    background: radial-gradient(ellipse at 60% 50%, var(--photo-a) 0%, var(--photo-b) 55%, rgba(15,24,34,0) 75%);
    opacity: .75;
  }
  .frame {
    position: absolute; left: 25px; top: 31px; width: 798px; height: 1117px;
    border: 1.5px solid var(--ink);
  }
  .title-tab { position: absolute; left: 58px; top: 23px; width: 310px; height: 46px; }
  .title-tab .label {
    position: absolute; left: 31px; top: 0; height: 46px; line-height: 46px;
    font-family: "Exo 2", sans-serif; font-style: italic; font-weight: 900;
    font-size: 26px; letter-spacing: 0.5px; color: var(--tab-ink);
  }
  .divider { position: absolute; left: 679px; top: 165px; width: 1px; height: 766px; background: var(--rule); }
  .intro {
    position: absolute; left: 51px; top: 111px; width: 660px;
    font-size: 17.5px; line-height: 22px;
  }
  .item { position: absolute; left: 51px; width: 746px; }
  .item .name, .item .kicker { font-size: 17.5px; line-height: 22px; }
  .item .desc { font-size: 14.6px; line-height: 22px; width: 560px; }
  .item .price {
    position: absolute; right: 0; font-size: 17.5px; line-height: 22px; text-align: right;
  }
  .item .price.short { right: 20px; }
  .notes {
    position: absolute; left: 51px; top: 1029px;
    font-family: "Montserrat", sans-serif; font-weight: 600; font-size: 15.6px; line-height: 20.5px;
  }
  .notes .soon { margin-top: 21px; }
</style>
</head>
<body>
<main class="page">
  <div class="hero-photo" role="img" aria-label="Dunkel abgetöntes Foto eines Burgers mit Sesambrötchen, Salat und Tomate"></div>
  <div class="frame"></div>

  <div class="title-tab">
    <svg width="310" height="46" viewBox="0 0 310 46" aria-hidden="true">
      <polygon points="30,0 310,0 282,46 0,46" fill="#ffffff"/>
    </svg>
    <span class="label">BURGERSEITE</span>
  </div>

  <p class="intro">hausgemachten Burgerbrötchen mit 6 wertvollen Urgetreidesorten, wahlweise mit SportsBar Fries, Wedges oder Süßkartoffel Fries (+1€)</p>

  <div class="divider"></div>

  <section class="item" style="top:176px">
    <span class="price short">9,50€</span>
    <h2 class="name">XL Classic Burger</h2>
    <p class="desc">180gramm Rinderhackfleisch mit Zwiebeln, Gurken und Tomate</p>
  </section>
  <section class="item" style="top:242px">
    <span class="price short">9,80€</span>
    <h2 class="name">XL SportsBar Burger</h2>
    <p class="desc">180gramm Rinderhackfleisch mit Zwiebeln, Gurken, Tomate &amp; Käse</p>
  </section>
  <section class="item" style="top:307px">
    <span class="price">10,50€</span>
    <h2 class="name">XL Chicken Burger</h2>
    <p class="desc" style="width:600px">180gramm saftig, zartes Hähnchenbrustfilet mit Zwiebeln, Gurken Tomate &amp; Käse</p>
  </section>
  <section class="item" style="top:373px">
    <span class="price">10,50€</span>
    <h2 class="name">XL Ahornburger</h2>
    <p class="desc">180gramm Rinderhackfleisch mit Speck, Zwiebeln, Gurken, Tomate &amp; Käse</p>
  </section>
  <section class="item" style="top:439px">
    <span class="price">10,50€</span>
    <h2 class="name">XL BBQ Burger</h2>
    <p class="desc" style="width:600px;font-size:13.8px">180gramm Rinderhackfleisch mit Zwiebeln, Gurken, Tomate, Käse &amp; rauchiger BBQ Soße</p>
  </section>
  <section class="item" style="top:505px">
    <p class="kicker">Unsere Besonderen !</p>
    <span class="price" style="top:22px">13,90€</span>
    <h2 class="name">XL Gourmet Burger</h2>
    <p class="desc">Ein außergewöhnliches Genuss-Erlebnis aus 200g reinem Fleisch vom amerikanischen Weiderind. Mit Zwiebeln, Gurken, Tomate &amp; Käse</p>
  </section>
  <section class="item" style="top:614px">
    <span class="price">13,90€</span>
    <h2 class="name">XL Iberico Burger</h2>
    <p class="desc">200 gramm delikates Fleisch mir dem besonderen Nussaroma des schwarzen Iberico Schweins. Garniert mit Zwiebeln, Gurken, Tomaten &amp; Käse</p>
  </section>
  <section class="item" style="top:702px">
    <span class="price">13,90€</span>
    <h2 class="name">XL Dry Aged Burger</h2>
    <p class="desc" style="width:600px">200 gramm Dry Aged Beef vom irischen Weiderind, 35 Tage am Knochen gereift. Garniert mit Salatblatt, Zwiebeln, Gurken, Tomate &amp; Käse</p>
  </section>
  <section class="item" style="top:789px">
    <span class="price">14,50€</span>
    <h2 class="name">XL Bison Burger</h2>
    <p class="desc" style="width:600px">200 gramm mageres Bisonfleisch aus Kanada. Ein erstaunliches<br>Geschmackserlebnis. Abgerundet mit Salatblatt, Zwiebeln, Gurken, Tomate &amp; Käse</p>
  </section>
  <section class="item" style="top:877px">
    <span class="price">18,98€</span>
    <h2 class="name">XXXXXL Ahorntower Burger</h2>
    <p class="desc">Ein luftig-warmes Burgerbrötchen, 980 gramm reines Rinderhackfleisch,<br>frischer Salat, Zwiebeln ,Gurken, saftige Speckscheiben, Tomaten, reichlich<br>Käse und unserer leckeren Burger Sauce. Ausserdem: Bei jeder Bestellung<br>gibt’s ein Foto und nach kompletten Verzehr winkt ein Platz in der Burger<br>Wall of Fame auf unserer Fanpage!</p>
  </section>

  <div class="notes">
    <p>Alle XL Burger auch als XXL mit 380 gramm Rinderhackfleisch &nbsp;+ 3€</p>
    <p>Unsere Gourmet Burger gibt es bereits ab 4,50€ als XXL mit jeweils 400 Gramm</p>
    <p>Unsere Vegetarischen Burger:</p>
    <p class="soon">Folgt</p>
  </div>
</main>
</body>
</html>
```